Letterhead That Inspires Trust

Birchwell Deed Services, LLC, (BDS) fixes technical problems with property deeds. The problems usually surface when someone tries to buy, sell or mortgage a piece of real estate and one of the lawyers involved find a title defect (a lien, an undischarged mortgage, a deceased person still on the title, unpaid taxes, etc.). BDS then gets involved and often has to contact prior property owners to get them to sign paperwork fixing the problem. We need a letterhead that will a) convey the seriousness of what we are trying to do, b) cause the recipients of our letters to recognize the importance of what are trying to do, and c) convey that we are a established and trustworthy company. We want it to include an image that suggests we are a problem solving company. Attached is an image we think might work; you can use it or not. In addition to our name (Birchwell Deed Services, LLC), the letterhead must include our address and phone number: 418 Calder Avenue, Suite 207, Providence, RI 02917 (401) 555-0372. We are thinking something straightforward without unnecessary colors or graphics.

```html
<!DOCTYPE html>
<html lang="en">
<head>
<meta charset="utf-8">
<title>Birchwell Deed Services — Letterhead</title>
<link rel="stylesheet" href="https://fonts.googleapis.com/css2?family=Arimo:wght@400&family=Roboto:wght@400;500&family=Pinyon+Script&display=swap">
<style>
  :root {
    --backdrop: #e4e4e4;
    --paper: #f3f3f3;
    --brand-grey: #6f6f6f;
    --contact-grey: #777777;
    --ink: #1c1c1c;
    --art-light: #f1f1f1;
    --art-mid: #dadada;
  }
  * { margin: 0; padding: 0; box-sizing: border-box; }
  html, body {
    width: 1200px; height: 1200px; overflow: hidden;
    background: var(--backdrop);
  }
  .letterhead {
    position: absolute; left: 211px; top: 50px;
    width: 778px; height: 1100px;
    background: var(--paper);
    box-shadow: 0 2px 10px rgba(0,0,0,0.12);
    overflow: hidden;
  }
  .brand {
    position: absolute; left: 64px; top: 52px;
    display: flex; align-items: center; gap: 12px;
    font-family: "Roboto", sans-serif; font-weight: 500;
    color: var(--brand-grey);
  }
  .brand-mark {
    width: 14px; height: 14px; background: var(--brand-grey);
  }
  .brand-name {
    font-size: 17px; line-height: 19px; letter-spacing: 0.5px;
    text-transform: uppercase;
  }
  .contact {
    position: absolute; right: 64px; top: 56px;
    text-align: right;
    font-family: "Roboto", sans-serif; font-size: 12.5px; line-height: 16px;
    color: var(--contact-grey);
  }
  .contact-phone {
    font-weight: 500; display: inline-flex; align-items: center; gap: 4px;
  }
  .contact-phone svg { width: 10px; height: 10px; }
  .contact-rule {
    width: 46px; height: 3px; background: var(--brand-grey);
    margin: 12px 0 0 auto;
  }
  .letter {
    position: absolute; left: 83px; top: 260px; width: 612px;
    font-family: "Arimo", sans-serif; font-size: 12.3px; line-height: 18.3px;
    color: var(--ink);
  }
  .letter-date { margin-bottom: 18px; }
  .recipient { margin-bottom: 36px; }
  .salutation { margin-bottom: 18px; }
  .letter-body p { text-align: justify; margin-bottom: 18px; }
  .closing { margin-top: 55px; }
  .signature {
    font-family: "Pinyon Script", cursive; font-size: 25px; line-height: 34px;
    margin-top: 2px;
  }
  .feature-art {
    position: absolute; right: 0; bottom: 0;
    width: 440px; height: 250px;
    background: radial-gradient(ellipse at 60% 60%, var(--art-mid) 0%, var(--art-light) 55%, var(--paper) 80%);
  }
</style>
</head>
<body>
<main class="letterhead">
  <header>
    <div class="brand">
      <span class="brand-mark"></span>
      <div class="brand-name">Birchwell<br>Deed<br>Services</div>
    </div>
    <address class="contact" style="font-style:normal">
      <div class="contact-phone">(401) 555-0372
        <svg viewBox="0 0 24 24" aria-hidden="true"><path fill="currentColor" d="M6.6 10.8a15.1 15.1 0 0 0 6.6 6.6l2.2-2.2a1 1 0 0 1 1-.25 11.4 11.4 0 0 0 3.6.57 1 1 0 0 1 1 1V20a1 1 0 0 1-1 1A17 17 0 0 1 3 4a1 1 0 0 1 1-1h3.5a1 1 0 0 1 1 1c0 1.25.2 2.45.57 3.57a1 1 0 0 1-.25 1z"/></svg>
      </div>
      <div>418 Calder Avenue, Suite 207</div>
      <div>Providence, RI 02917</div>
      <div class="contact-rule"></div>
    </address>
  </header>

  <section class="letter">
    <p class="letter-date">01 January 2050</p>
    <p class="recipient">Company (Pvt) Ltd.<br>PO Box 3355 Mainville St<br>Sample City Country 3355</p>
    <p class="salutation">Dear Martin Halloway,</p>
    <div class="letter-body">
      <p>Lorem ipsum dolor sit amet, consectetuer adipiscing elit, sed diam nonummy nibh euismod tincidunt ut laoreet dolore magna aliquam erat volutpat. Ut wisi enim ad minim veniam, quis nostrud exerci tation ullamcorper suscipit lobortis nisl ut aliquip ex ea commodo consequat. Duis dolore te feugait nulla facilisi. Nam liber tempor cum soluta nobis eleifend option congue nihil imperdiet doming id quod mazim placerat facer possim assum. Lorem ipsum dolor sit amet, consectetuer adipiscing elit, sed diam nonummy nibh euismod tincidunt ut laoreet dolore magna aliquam erat volutpat. Ut wisi enim ad minim veniam, quis nostrud exerci tation ullamcorper suscipit lobortis nisl ut aliquip ex ea commodo consequat.</p>
      <p>Consectetuer adipiscing elit, sed diam nonummy nibh euismod tincidunt ut laoreet dolore magna aliquam erat volutpat. Ut wisi enim ad minim veniam, quis nostrud exerci tation ullamcorper suscipit lobortis nisl ut aliquip ex ea commodo consequat. Consectetuer adipiscing elit, sed diam nonummy nibh euismod tincidunt ut laoreet dolore magna aliquam erat volutpat. Ut wisi enim ad minim veniam, quis nostrud exerci tation ullamcorper suscipit lobortis nisl ut aliquip ex ea commodo consequat.</p>
      <p>Consectetuer adipiscing elit, sed diam nonummy nibh euismod tincidunt ut laoreet dolore magna aliquam erat volutpat. Ut wisi enim ad minim veniam, quis nostrud exerci tation ullamcorper suscipit lobortis nisl ut aliquip ex ea commodo consequat. Consectetuer adipiscing elit, sed diam nonummy nibh euismod tincidunt ut laoreet dolore magna aliquam erat volutpat. Ut wisi enim ad minim veniam, quis nostrud exerci tation ullamcorper suscipit lobortis nisl ut aliquip ex ea commodo consequat.</p>
    </div>
    <p class="closing">Sincerely Yours</p>
    <p class="signature">Edwin Carrow</p>
  </section>

  <div class="feature-art" role="img" aria-label="Pale photograph of small wooden figures standing in groups, joined by lines across a surface of tangled threads, suggesting problems being connected and solved"></div>
</main>
</body>
</html>
```